Business Card Design Project

Please refer to this project for further instructions: http://tasks.pixelmarlo.com/task.aspx?id=918274

Industry/Entity Type

Business

```html
<!DOCTYPE html>
<html lang="en">
<head>
<meta charset="utf-8">
<title>Fieldmere – Business Card</title>
<link rel="stylesheet" href="https://fonts.googleapis.com/css2?family=Roboto+Condensed:wght@300;400;700&display=swap">
<style>
  :root {
    --green-light: #86c140;
    --green-mid: #3f9a3c;
    --green-deep: #0a6a37;
    --green-ink: #0f6e38;
    --edge-green: #8dc63f;
    --white: #ffffff;
  }
  html, body {
    margin: 0;
    padding: 0;
    width: 1200px;
    height: 686px;
    overflow: hidden;
    background: #ffffff;
  }
  .card {
    position: relative;
    width: 1200px;
    height: 686px;
    overflow: hidden;
    font-family: "Roboto Condensed", "Arial Narrow", sans-serif;
    color: var(--white);
    background:
      radial-gradient(ellipse 55% 70% at 58% 30%, var(--green-deep) 0%, rgba(10,106,55,0) 100%),
      linear-gradient(160deg, var(--green-light) 0%, var(--green-mid) 18%, var(--green-deep) 45%, var(--green-deep) 60%, var(--green-mid) 82%, var(--green-light) 100%);
  }
  .card__swoosh {
    position: absolute;
    inset: 0;
    width: 1200px;
    height: 686px;
  }
  .brand {
    position: absolute;
    left: 304px;
    top: 344px;
    transform: translate(-50%, -50%);
    display: flex;
    align-items: center;
    gap: 14px;
    color: var(--green-ink);
    font-weight: 700;
    font-size: 54px;
    letter-spacing: 2px;
    white-space: nowrap;
  }
  .brand__dot {
    width: 28px;
    height: 28px;
    border-radius: 50%;
    background: var(--green-ink);
  }
  .holder {
    position: absolute;
    left: 624px;
    top: 140px;
    margin: 0;
    font-size: 43px;
    font-weight: 300;
    letter-spacing: 0.5px;
  }
  .holder__company { font-weight: 700; }
  .contact {
    position: absolute;
    left: 624px;
    top: 370px;
    margin: 0;
    padding: 0;
    list-style: none;
    font-size: 41px;
    font-weight: 300;
    line-height: 56px;
  }
  .contact__label { font-weight: 700; }
</style>
</head>
<body>
  <main class="card">
    <svg class="card__swoosh" viewBox="0 0 750 429" aria-hidden="true">
      <path d="M0,170 C40,90 150,50 240,62 C320,75 365,150 355,230 C345,300 290,345 200,360 C140,372 110,380 95,392 C140,384 220,378 320,388 C250,396 150,406 80,429 L0,429 Z"
            fill="var(--white)" stroke="var(--edge-green)" stroke-width="6" stroke-linejoin="round"/>
    </svg>

    <div class="brand">
      <span class="brand__dot"></span>
      <span class="brand__name">FIELDMERE</span>
    </div>

    <p class="holder"><span class="holder__company">FIELDMERE</span> - Owner</p>

    <ul class="contact">
      <li><span class="contact__label">M -</span> 555-014-2873</li>
      <li><span class="contact__label">E -</span> hello@fieldmere.com</li>
      <li><span class="contact__label">W -</span> www.fieldmere.com</li>
    </ul>
  </main>
</body>
</html>
```